Web site design for news feed - Talvren Live

We need to design a webpage to promote our web scraping newsfeed (similar to pagewheel) the name of the business is "Talvren Live" ( a subsidiary of our company Talvren - see www.corvel-holdings.example for details, DO NOT BASE THAT WEBSITE ON YOUR DESIGN).

We are inspired by famous Economists, we are inspired by empirical data, accuracy, but importantly the site needs to portray our "new approach" to delivering functional and "boring" financial news flow (pagewheel)

Websites we like:

www.zolvo.example - love the graphics
www.pagewheel.example - love the functionality
http://www.marketdial.example/ - practical
http://www.wirepost.example/ - practical
http://www.quenbrix.example/en-us/default.aspx
www.ldg.example
http://www.harbortimes.example/
www.velto.example

Our logo is attached

We like black and white, artful, mabel tunn etc
Updates

Hi All, please bear in mind that this is a NEWS site (it will need space to post stories) - so whilst the visual aspect is really important, the functionally around the amount of stories we can post is important too.

think marketdial.example, www.pitcrest.example, www.ldg.example - but feel (creativity) is zolvo.example, pagewheel.example

thanks all for some great designs.

i will revert to those closest tomorrow.
in the meantime, please bear in mind that the vision of skylines and economists helps me get to the design immediately, it resonates better, it helps me visually decide. 
lastly, in terms of the news "spaces", i will need to have 6 "top stories" and then room for maybe 20 more headlines..the top stories will need a picture, the 20 others will not (just headline text).
Thanks everyone again

Industry/Entity Type

Financial

Font styles to use
Serif
Sans Serif

```html
<!DOCTYPE html>
<html lang="en">
<head>
<meta charset="utf-8">
<title>Talvren Live</title>
<link rel="stylesheet" href="https://fonts.googleapis.com/css2?family=Open+Sans:wght@400;600;700;800&display=swap">
<style>
:root{
  --stage:#b2b2b2;
  --page:#ffffff;
  --ink:#3a3a3a;
  --muted:#9a9a9a;
  --black:#0c0c0c;
  --rule:#cfcfcf;
  --tab-gray:#6a6a6a;
  --side-gray:#b9b9b9;
  --side-dark:#4b4b4b;
  --brand-mark:#e8a21c;
  --brand-name:#7e8488;
  --up:#3d9a1c;
  --down:#c0312b;
}
*{margin:0;padding:0;box-sizing:border-box}
html,body{width:856px;height:1200px;overflow:hidden}
body{background:var(--stage);font-family:"Open Sans",Arial,sans-serif;color:var(--ink);position:relative}
.abs{position:absolute}
.page{left:50px;top:10px;width:750px;height:1152px;background:var(--page);box-shadow:0 2px 6px rgba(0,0,0,.35)}
.topbar{left:50px;top:14px;width:750px;height:36px;background:linear-gradient(#2a2a2a,#050505)}
.nav{display:flex;align-items:center;top:14px;left:490px;height:36px;color:#fff;font-size:9.5px}
.nav span{padding:0 22px}
.nav .sep{width:1px;height:16px;background:#888;padding:0}
.search{left:649px;top:26px;width:139px;height:18px;background:#fff;border-radius:9px;font-size:8.5px;color:#bbb;padding:3px 0 0 52px}
.search svg{position:absolute;right:6px;top:3px}
.brand{left:70px;top:64px;display:flex;align-items:center;gap:18px}
.brand-mark{width:64px;height:64px;background:var(--brand-mark)}
.brand-name{font-size:36px;line-height:38px;color:var(--brand-name);font-weight:400;width:120px}
.intro{left:292px;top:67px;width:476px;font-size:9.4px;line-height:12.4px;text-align:justify;color:#222}
.rule{height:1px;background:var(--rule)}
.top-label{left:62px;top:186px;font-size:36px;font-weight:800;line-height:31px;letter-spacing:-1px}
.top-label .a{color:var(--ink)}
.top-label .b{color:#b5b5b5;font-size:27px}
.photo-frame{left:162px;top:188px;width:374px;height:214px;background:#fff;box-shadow:0 2px 5px rgba(0,0,0,.35)}
.photo{left:170px;top:194px;width:361px;height:204px;background:linear-gradient(180deg,#1e2634 0%,#39465a 35%,#27303c 60%,#0e1218 100%)}
.dots{left:276px;top:418px}
.side-headline{left:551px;top:188px;width:217px}
.side-headline h2{font-size:19px;font-weight:700;color:var(--ink);margin-bottom:6px}
.side-headline p{font-size:9.4px;line-height:13.6px;text-align:justify;hyphens:auto;color:#333}
.side-headline .body{height:163px;overflow:hidden}
.side-headline .more{font-size:9px;font-weight:700;margin-top:12px}
.social{left:801px;top:234px;width:25px;height:168px;background:var(--black)}
.section-title{font-size:14px;font-weight:700;color:var(--ink);letter-spacing:.2px}
.section-title span{color:var(--muted)}
.market{left:50px;top:466px;width:750px;height:204px;background:linear-gradient(#0a0a0a,#2a2a2a)}
.tabs{left:71px;top:474px;width:318px;height:20px;display:flex;color:#fff;font-size:9.5px;align-items:center}
.tabs span{padding:0 12px;border-right:1px solid #666}
.tabs span:last-child{border:none}
.index-bar{left:71px;top:497px;width:318px;height:16px;background:var(--tab-gray);color:#fff;font-size:8.5px;padding:2px 0 0 10px}
.chart{left:71px;top:513px;width:318px;height:145px;background:#000}
.quotes{left:403px;top:518px;width:379px}
.quote{display:flex;align-items:center;height:16.5px;border-bottom:1px solid #3a3a3a;color:#fff;font-size:10.5px}
.quote .name{width:106px;padding-left:2px}
.quote .val{width:56px}
.badge{width:59px;height:13px;border-radius:3px;font-size:10px;text-align:center;line-height:13px}
.badge.up{background:var(--up)}
.badge.down{background:var(--down)}
.more-data{left:331px;top:670px;width:191px;height:20px;background:#1f1f1f;border-radius:0 0 10px 10px;color:#fff;font-size:9.5px;font-weight:700;text-align:center;padding-top:3px}
.story{width:231px}
.story h3{font-size:11px;font-weight:700;color:var(--ink);padding-bottom:4px;border-bottom:1px solid var(--rule);margin-bottom:4px}
.story p{font-size:9.4px;line-height:12.2px;text-align:justify;hyphens:auto;height:48px;overflow:hidden;color:#333}
.story .more{font-size:9px;font-weight:700;margin-top:4px}
.aside{left:566px;top:721px;width:215px;height:331px;background:var(--side-gray)}
.aside-title{height:33px;background:#c9c9c9;font-size:9px;font-weight:700;color:#444;text-align:center;line-height:33px}
.aside-space{height:98px;background:var(--side-dark);color:#fff;font-size:9px;font-style:italic;text-align:center;line-height:98px}
.aside p{font-size:9.4px;line-height:12.2px;text-align:justify;hyphens:auto;padding:6px 10px 0;height:196px;overflow:hidden;color:#222}
.pager{left:480px;top:1033px;font-size:8.5px;color:#333}
.footer{left:50px;top:1070px;width:750px;height:92px;background:linear-gradient(#1a1a1a,#000)}
.footer-links{left:252px;top:1106px;display:flex;color:#fff;font-size:11px;align-items:center}
.footer-links span{padding:0 10px;border-right:1px solid #777}
.footer-links span:first-child{padding-left:12px}
.footer-links span:last-child{border:none}
.more-content{left:657px;top:1108px;color:#fff;font-size:11px}
.copyright{left:0;top:1172px;width:856px;text-align:center;font-size:10px;color:#8a8a8a}
</style>
</head>
<body>
<div class="abs page"></div>

<header>
  <div class="abs topbar"></div>
  <nav class="abs nav"><span>HOME</span><i class="sep"></i><span>CONTACT</span></nav>
  <div class="abs search">search
    <svg width="12" height="12" viewBox="0 0 12 12"><circle cx="5" cy="5" r="3.6" fill="none" stroke="#999" stroke-width="1.3"/><line x1="7.6" y1="7.6" x2="11" y2="11" stroke="#999" stroke-width="1.5"/></svg>
  </div>
  <div class="abs brand"><div class="brand-mark"></div><div class="brand-name">Talvren Live</div></div>
  <p class="abs intro" lang="en">Talvren is an external investment manager and advisor on macroeconomic investment themes and portfolio construction for institutional investors. It serves multi-product asset managers, sovereign wealth funds, hedge funds, and pension funds by offering fundamental and technical cross-asset analysis that is heavily influenced by quantitative evidence. While traditional advisors and external fund managers have incentives to chase beta, Talvren measures its success solely through alpha generation for its clients.</p>
  <div class="abs rule" style="left:50px;top:174px;width:750px"></div>
</header>

<section class="top-news">
  <div class="abs top-label"><div class="a">TOP</div><div class="b">NEWS</div></div>
  <div class="abs photo-frame"></div>
  <div class="abs photo" role="img" aria-label="Night skyline of a harbour city with lit towers"></div>
  <svg class="abs dots" width="160" height="14" viewBox="0 0 160 14">
    <polygon points="6,2 6,12 0,7" fill="#ccc"/>
    <g fill="#d4d4d4" stroke="#bdbdbd"><circle cx="24" cy="7" r="5.2"/><circle cx="42" cy="7" r="5.2"/><circle cx="60" cy="7" r="5.2"/><circle cx="78" cy="7" r="5.2"/><circle cx="96" cy="7" r="5.2"/><circle cx="114" cy="7" r="5.2"/><circle cx="132" cy="7" r="5.2"/></g>
    <polygon points="148,2 148,12 154,7" fill="#ccc"/>
  </svg>
  <article class="abs side-headline" lang="en">
    <h2>HEADLINES</h2>
    <div class="body">
      <p>Lorem ipsum dolor sit amet, consectetuer adipiscing elit, sed diam nonummy nibh euismod tincidunt ut laoreet dolore magna aliquam erat volutpat. Ut wisi enim ad minim veniam, quis nostrud exerci tation ullamcorper suscipit lobortis nisl ut aliquip ex ea commodo consequat. Duis autem vel eum iriure dolor in hendrerit in vulputate velit esse molestie consequat, vel illum dolore eu feugiat nulla facilisis at vero eros et accumsan et iusto odio dignissim qui blandit praesent luptatum zzril delenit</p>
      <p>consequat, vel illum dolore eu feugiat nulla facilisis at vero eros et accumsan et iusto odio dignissim.</p>
    </div>
    <div class="more">read more</div>
  </article>
  <div class="abs rule" style="left:50px;top:440px;width:750px"></div>
</section>

<aside class="abs social">
  <svg width="25" height="168" viewBox="0 0 25 168">
    <circle cx="12.5" cy="22" r="6" fill="#fff"/>
    <circle cx="12.5" cy="62" r="6" fill="#fff"/>
    <circle cx="12.5" cy="102" r="6" fill="#fff"/>
    <rect x="5" y="137" width="15" height="11" fill="#fff"/>
    <polyline points="5,137 12.5,143 20,137" fill="none" stroke="#999" stroke-width="1"/>
  </svg>
</aside>

<section class="market-review">
  <div class="abs section-title" style="left:73px;top:446px">MARKET<span>REVIEW</span></div>
  <div class="abs market"></div>
  <div class="abs tabs"><span>OVERVIEW</span><span>US</span><span>EUROPE</span><span>ASIA</span><span>COMMODITIES</span></div>
  <div class="abs index-bar">▼ CRIA</div>
  <div class="abs chart"></div>
  <div class="abs quotes">
    <div class="quote"><span class="name">▸ Bolt 500</span><span class="val">0.000.000</span><span class="badge up">0.000.000</span></div>
    <div class="quote"><span class="name">▸ Arlen 100</span><span class="val">0.000.000</span><span class="badge up">0.000.000</span></div>
    <div class="quote"><span class="name">▸ Kesho 225</span><span class="val">0.000.000</span><span class="badge up">0.000.000</span></div>
    <div class="quote"><span class="name">▸ Crued Oil (WTI)</span><span class="val">0.000.000</span><span class="badge down">0.000.000</span></div>
    <div class="quote"><span class="name">▸ Gold</span><span class="val">0.000.000</span><span class="badge down">0.000.000</span></div>
  </div>
  <div class="abs more-data">more data &nbsp;▼</div>
</section>

<section class="latest" lang="en">
  <div class="abs rule" style="left:50px;top:696px;width:750px"></div>
  <div class="abs section-title" style="left:73px;top:702px">LATEST <span>HEADLINES</span></div>
  <div class="abs rule" style="left:50px;top:720px;width:750px"></div>

  <article class="abs story" style="left:73px;top:739px"><h3>HEADLINES</h3><p>Lorem ipsum dolor sit amet, consectetuer adipiscing elit, sed diam nonummy nibh euismod tincidunt ut laoreet dolore magna aliquam erat volutpat. Ut wisi enim ad minim veniam, quis nostrud</p><div class="more">read more</div></article>
  <article class="abs story" style="left:318px;top:739px"><h3>HEADLINES</h3><p>Lorem ipsum dolor sit amet, consectetuer adipiscing elit, sed diam nonummy nibh euismod tincidunt ut laoreet dolore magna aliquam erat volutpat. Ut wisi enim ad minim veniam, quis nostrud</p><div class="more">read more</div></article>
  <article class="abs story" style="left:73px;top:837px"><h3>HEADLINES</h3><p>Lorem ipsum dolor sit amet, consectetuer adipiscing elit, sed diam nonummy nibh euismod tincidunt ut laoreet dolore magna aliquam erat volutpat. Ut wisi enim ad minim veniam, quis nostrud</p><div class="more">read more</div></article>
  <article class="abs story" style="left:318px;top:837px"><h3>HEADLINES</h3><p>Lorem ipsum dolor sit amet, consectetuer adipiscing elit, sed diam nonummy nibh euismod tincidunt ut laoreet dolore magna aliquam erat volutpat. Ut wisi enim ad minim veniam, quis nostrud</p><div class="more">read more</div></article>
  <article class="abs story" style="left:73px;top:934px"><h3>HEADLINES</h3><p>Lorem ipsum dolor sit amet, consectetuer adipiscing elit, sed diam nonummy nibh euismod tincidunt ut laoreet dolore magna aliquam erat volutpat. Ut wisi enim ad minim veniam, quis nostrud</p><div class="more">read more</div></article>
  <article class="abs story" style="left:318px;top:934px"><h3>HEADLINES</h3><p>Lorem ipsum dolor sit amet, consectetuer adipiscing elit, sed diam nonummy nibh euismod tincidunt ut laoreet dolore magna aliquam erat volutpat. Ut wisi enim ad minim veniam, quis nostrud</p><div class="more">read more</div></article>

  <div class="abs pager">1 · 2 · 3 · 4 · 5 · 6</div>

  <aside class="abs aside">
    <div class="aside-title">ARTICLE/ARCHIVE/OPINION/ VIDEO SPACE</div>
    <div class="aside-space">Free Space ( you can take out if you no need)</div>
    <p>Lorem ipsum dolor sit amet, consectetuer adipiscing elit, sed diam nonummy nibh euismod tincidunt ut laoreet dolore magna aliquam erat volutpat. Ut wisi enim ad minim veniam, quis nostrud exerci tation ullamcorper suscipit lobortis nisl ut aliquip ex ea commodo consequat. Duis autem vel eum iriure dolor in hendrerit in vulputate velit esse molestie consequat, vel illum dolore eu feugiat nulla facilisis at vero eros et accumsan et iusto odio dignissim qui blandit praesent luptatum zzril delenit consequat, vel illum dolore eu feugiat nulla facilisis at vero eros et accumsan et iusto</p>
  </aside>
  <div class="abs rule" style="left:50px;top:1056px;width:750px"></div>
</section>

<footer>
  <div class="abs footer"></div>
  <div class="abs footer-links"><span>Archive</span><span>Trademarks</span><span>Terms of Service</span><span>Privacy Policy</span></div>
  <div class="abs rule" style="left:614px;top:1106px;width:1px;height:20px;background:#777"></div>
  <div class="abs more-content">more content</div>
  <svg class="abs" style="left:742px;top:1106px" width="29" height="20" viewBox="0 0 29 20">
    <rect x="0.5" y="0.5" width="28" height="19" fill="#fff" stroke="#999"/>
    <polyline points="1,1 14.5,11 28,1" fill="none" stroke="#999"/>
  </svg>
  <div class="abs copyright">©2013 Talvren Live. All Rights Reserved</div>
</footer>
</body>
</html>
```